Teams Background for client video calls - giving them a feel who we are

I'm keen to create a background artwork of a modern dynamic office that also reflects our values which are all about transparency, humility, integrity etc. Our company is called Quenby Collective. Our behaviours are agility, excellence and precision. You can find all about our colours and branding under our website www.quenbycollective.com

Target Market(s)

IT Recruitment

Industry/Entity Type

IT Recruitment

Font styles to use
Other font styles liked:
• as per our website www.quenbycollective.com

Colors
0054AA
0677BA
7BADD7
CADEEF
E8F1F8

Requirements
Must have
• A modern cool dynamic work office design incooperating our logo and what we stand for in terms of colours and our values and behaviours we live as a company. As i founded the office in the cabin but now we are in a modern office a blend would work i think.

```html
<!DOCTYPE html>
<html lang="en">
<head>
<meta charset="utf-8">
<title>Quenby Collective – Call Background</title>
<link rel="stylesheet" href="https://fonts.googleapis.com/css2?family=Barlow+Condensed:wght@600;700&display=swap">
<style>
  :root {
    --navy: #102a5c;
    --blue-deep: #1d3a78;
    --blue-mid: #4a68a8;
    --wall: #7a90c2;
    --floor: #8a8aa0;
    --warm: #b79e6c;
    --white: #ffffff;
    --accent-gold: #f6b21a;
    --accent-teal: #12a59b;
    --line-teal: #0f8c8f;
  }
  * { margin: 0; padding: 0; box-sizing: border-box; }
  html, body { width: 1200px; height: 675px; overflow: hidden; background: var(--navy); }
  .canvas {
    position: relative;
    width: 1200px;
    height: 675px;
    overflow: hidden;
    font-family: "Barlow Condensed", "Arial Narrow", sans-serif;
  }
  .office-scene {
    position: absolute;
    inset: 0;
    background:
      radial-gradient(ellipse 360px 200px at 610px 330px, rgba(150,170,215,0.55), rgba(150,170,215,0) 100%),
      radial-gradient(ellipse 300px 120px at 980px 610px, rgba(190,120,70,0.35), rgba(190,120,70,0) 100%),
      linear-gradient(90deg, rgba(16,42,92,0.55) 0%, rgba(16,42,92,0) 22%, rgba(16,42,92,0) 80%, rgba(16,42,92,0.35) 100%),
      linear-gradient(180deg, var(--navy) 0%, var(--blue-deep) 18%, var(--blue-mid) 34%, var(--wall) 52%, #5d76ad 60%, var(--floor) 82%, var(--warm) 100%);
  }
  .decor {
    position: absolute;
    inset: 0;
    width: 1200px;
    height: 675px;
  }
  .brand-name {
    position: absolute;
    left: 62px;
    top: 102px;
    color: var(--white);
    font-weight: 700;
    font-size: 48px;
    line-height: 42px;
    letter-spacing: 0.5px;
  }
  .quote-rule {
    position: absolute;
    left: 60px;
    top: 277px;
    width: 3px;
    height: 398px;
    background: var(--accent-gold);
  }
  .headline {
    position: absolute;
    left: 100px;
    top: 302px;
    color: var(--white);
    font-weight: 700;
    font-size: 41px;
    line-height: 39.5px;
    text-transform: uppercase;
    letter-spacing: -0.2px;
  }
</style>
</head>
<body>
<main class="canvas">
  <div class="office-scene" role="img" aria-label="Photo of a bright modern meeting room with a long table, blue office chairs, potted plants, wall screens and an orange pouf, under a blue tint"></div>

  <svg class="decor" viewBox="0 0 1200 675" aria-hidden="true">
    <defs>
      <path id="quote-glyph" d="M0,11 Q0,1 11,0 L12,5 Q6,6 6,11 L12,11 L12,24 L0,24 Z"/>
    </defs>
    <polygon points="430,0 470,0 300,675 250,675" fill="#ffffff" opacity="0.06"/>
    <polygon points="740,0 820,0 620,675 540,675" fill="#ffffff" opacity="0.05"/>
    <line x1="708" y1="67.5" x2="1200" y2="67.5" stroke="var(--line-teal)" stroke-width="3"/>
    <g fill="none" stroke="var(--accent-teal)" stroke-width="4">
      <circle cx="1194" cy="517" r="64"/>
      <circle cx="1160" cy="640" r="113"/>
      <circle cx="1006" cy="730" r="97"/>
    </g>
    <g class="quote-open" fill="var(--accent-gold)" transform="translate(72,277)">
      <use href="#quote-glyph"/>
      <use href="#quote-glyph" x="15"/>
    </g>
    <g class="quote-close" fill="var(--accent-gold)" transform="translate(377,442) rotate(180)">
      <use href="#quote-glyph"/>
      <use href="#quote-glyph" x="15"/>
    </g>
  </svg>

  <div class="brand-name">Quenby<br>Collective</div>

  <div class="quote-rule"></div>
  <h1 class="headline">Enabling<br>Partnerships in<br>IT - Recruitment</h1>
</main>
</body>
</html>
```